Ecommerce site for Bramwell Dovey Company

This is an ecommerce store design and will be based on the xcart ecommerce platform, attached is a design specification and all images to use in the design, you may use any other images you see fit.
This is a new Company so has no logo, if possible please create a logo but if not just use a text based logo in the design this maybe replaced later if required.
We only require a Home page design initially but will also need a category and product page design created, if you can do those also it would be an advantage.
IMPORTANT
We require all designs to be supplied as a full size JPG so we can see the design in detail as the pixel quarry previews are often too small.

```html
<!DOCTYPE html>
<html lang="en">
<head>
<meta charset="utf-8">
<title>Dovey Rails – Home</title>
<link href="https://fonts.googleapis.com/css2?family=Arimo:wght@400;700&family=Caveat+Brush&display=swap" rel="stylesheet">
<style>
:root{
  --ink:#222;
  --muted:#555;
  --accent:#e0640a;
  --alert:#c8261a;
  --navbar:#0b0b0b;
  --stage:#0f1524;
  --silver-top:#f4f4f4;
  --silver-bot:#9a9a9a;
  --footer:#474747;
  --footer-field:#666;
  --base:#080808;
  --line:#d8d8d8;
}
*{box-sizing:border-box;margin:0;padding:0}
html,body{width:909px;height:1200px;overflow:hidden}
body{position:relative;background:#fff;font-family:Arimo,Arial,sans-serif;color:var(--ink)}
.abs{position:absolute}
.navbar{left:0;top:0;width:909px;height:42px;background:linear-gradient(#2b2b2b,var(--navbar));border-bottom:3px solid #333}
.nav a{position:absolute;top:14px;font-size:11px;color:#fff;text-decoration:none}
.nav .current{left:84px;top:7px;width:53px;height:28px;border:1px solid #555;border-radius:4px;background:#111;text-align:center;line-height:26px}
.lang{left:676px;top:14px;font-size:11px;color:#ddd}
.flag{left:742px;top:15px;width:16px;height:9px;background:linear-gradient(90deg,#1d3d8f 40%,#c8261a 40% 60%,#1d3d8f 60%)}
.stage{left:0;top:42px;width:909px;height:300px;background:radial-gradient(circle at 50% 30%,#1f2a40,var(--stage))}
.hero{left:79px;top:45px;width:746px;height:297px;background:linear-gradient(90deg,#4a4547,#b9b2ab 20%,#5b5555 35%,#cfc8c0 50%,#6a6363 65%,#bcb5ad 80%,#3f3b3c)}
.brand-plate{left:356px;top:45px;width:229px;height:126px}
.brand-name{left:356px;top:70px;width:229px;text-align:center;font-family:Arimo,Arial,sans-serif;font-weight:700;font-size:28px;color:#2a2a2a;letter-spacing:1px}
.arrow{width:32px;height:32px;border-radius:50%;background:linear-gradient(#fff,#bbb);border:2px solid #888}
.arrow svg{display:block;margin:6px}
.caption{left:79px;top:263px;width:746px;height:50px;background:rgba(40,40,48,.72);color:#fff;font-size:14px;line-height:22px;text-align:center;padding-top:3px}
.page-shadow{left:79px;top:342px;width:746px;height:560px;box-shadow:0 0 8px rgba(0,0,0,.25)}
.panel{top:342px;width:231px;height:117px}
.panel h2{position:absolute;left:0;top:8px;width:100%;text-align:center;font-family:"Caveat Brush",cursive;font-weight:400;font-size:19px;color:#333}
.panel .txt{position:absolute;font-size:9px;line-height:14px}
.panel .red{color:var(--alert)}
.search-field{left:22px;top:47px;width:153px;height:23px;border:1px solid #888;background:#ddd}
.go-btn{left:187px;top:47px;width:27px;height:23px;background:linear-gradient(#fff,#bbb);border:1px solid #999;font-size:9px;text-align:center;line-height:21px}
.svc li{list-style:none;font-size:9px;line-height:13.5px;padding-left:14px;position:relative}
.svc li::before{content:"";position:absolute;left:0;top:3px;border:4px solid transparent;border-left:6px solid #666}
.box{left:98px;width:225px;border:1px solid var(--line);border-radius:4px;background:#fff;box-shadow:0 0 3px rgba(0,0,0,.1)}
.box-head{position:absolute;left:5px;top:4px;width:213px;height:52px;background:#e9e9e9;border-radius:2px 2px 50% 50%/2px 2px 14px 14px;text-align:center;font-size:15px;padding-top:17px}
.cats{position:absolute;left:40px;top:64px;list-style:none}
.cats li{font-size:9px;height:18px;padding-left:18px;position:relative}
.cats li::before{content:"»";position:absolute;left:0;top:-4px;font-size:13px;font-weight:700}
.field{border:1px solid #888;background:#eee}
.btn{background:linear-gradient(#f3f3f3,#aaa);font-size:9px;text-align:center}
.welcome{left:360px;top:471px;font-family:"Caveat Brush",cursive;font-size:22px;color:#555}
.welcome small{font-size:14px}
.photo{border:1px solid #999;border-radius:3px}
.copy{font-size:9.5px;line-height:18px;color:var(--muted)}
.featured{left:370px;top:692px;font-size:14px;color:#555}
.product-text{font-size:9.5px;line-height:13px;color:#333}
.price{font-size:9px;color:#333}
.price b{font-size:18px;color:var(--accent);margin-left:8px}
.footer{left:82px;top:902px;width:741px;height:199px;background:var(--footer)}
.footer h3{position:absolute;font-weight:400;font-size:14px;color:#ddd;line-height:18px}
.footer .ff{background:var(--footer-field);position:absolute}
.footer ul{position:absolute;list-style:none;left:272px;top:54px}
.footer li{font-size:9px;color:#eee;height:23.3px;padding-left:12px;position:relative}
.footer li::before{content:"›";position:absolute;left:0;top:-3px;font-size:12px;font-weight:700}
.dark-btn{position:absolute;background:#111;border-radius:3px;color:#ddd;font-size:9px;text-align:center;border:1px solid #333}
.base{left:0;top:1103px;width:909px;height:97px;background:linear-gradient(#282828,var(--base))}
.badge{top:1128px;height:18px;width:30px;background:#dfe5f0;border:1px solid #999}
.social{top:1168px;width:18px;height:18px;border-radius:50%}
.legal{left:406px;top:1134px;font-size:9px;color:#ddd}
.copyright{left:447px;top:1157px;font-size:9px;color:#ddd}
</style>
</head>
<body>

<header class="abs navbar">
  <nav class="nav">
    <a class="current" href="#">HOME</a>
    <a style="left:151px" href="#">ABOUT US</a>
    <a style="left:225px" href="#">OUR SERVICES</a>
    <a style="left:322px" href="#">PRODUCTS</a>
    <a style="left:404px" href="#">GALLERY</a>
    <a style="left:475px" href="#">CONTACT US</a>
  </nav>
  <span class="abs lang">Language&nbsp;&nbsp;:</span>
  <span class="abs flag" role="img" aria-label="English language flag"></span>
</header>

<section class="abs stage"></section>
<div class="abs hero" role="img" aria-label="Slideshow photo of silver patterned curtains on a ceiling track"></div>

<svg class="abs brand-plate" viewBox="0 0 229 126" aria-hidden="true">
  <defs><linearGradient id="plate" x1="0" y1="0" x2="0" y2="1"><stop offset="0" stop-color="#fdfdfd"/><stop offset="1" stop-color="#9c9c9c"/></linearGradient></defs>
  <path d="M0 0H229V120Q170 80 114.5 96Q59 80 0 120Z" fill="url(#plate)"/>
  <path d="M0 120Q59 80 114.5 96Q170 80 229 120V126Q170 88 114.5 104Q59 88 0 126Z" fill="#e6e6e6"/>
</svg>
<div class="abs brand-name">DOVEY RAILS</div>

<div class="abs arrow" style="left:72px;top:192px"><svg width="16" height="16" viewBox="0 0 16 16"><path d="M8 3L3 8L8 13ZM14 3L9 8L14 13Z" fill="#222"/></svg></div>
<div class="abs arrow" style="left:807px;top:192px"><svg width="16" height="16" viewBox="0 0 16 16"><path d="M2 3L7 8L2 13ZM8 3L13 8L8 13Z" fill="#222"/></svg></div>

<p class="abs caption">Ketase mleie lerode miaseras rase lacheanrimaurillus lerasaetsm sociis natotibus etgnis disriea<br>jeserta eraeia laseratslertasekertalrurtas feugiat malesuadabi nunc leasea accumsan.</p>

<div class="abs page-shadow"></div>
<main class="abs" style="left:79px;top:342px;width:746px;height:560px;background:#fff"></main>

<svg width="0" height="0" style="position:absolute"><defs>
  <linearGradient id="silver" x1="0" y1="0" x2="0" y2="1"><stop offset="0" stop-color="#9e9e9e"/><stop offset=".35" stop-color="#f6f6f6"/><stop offset="1" stop-color="#b5b5b5"/></linearGradient>
</defs></svg>

<section class="abs panel" style="left:94px">
  <svg class="abs" width="231" height="117" viewBox="0 0 231 117" aria-hidden="true"><path d="M0 0H231V110Q115.5 58 0 110Z" fill="url(#silver)"/><path d="M0 110Q115.5 58 231 110V117Q115.5 66 0 117Z" fill="#ddd"/></svg>
  <h2>My Basket</h2>
  <p class="txt" style="left:29px;top:41px">NO OF ITEMS: 0<br>YOUR BASKET IS EMPTY</p>
  <p class="txt red" style="left:157px;top:42px">VALUE #0.00<br>CHECKOUT<br><span style="display:block;margin-top:2px">VIEW BASKET</span></p>
</section>

<section class="abs panel" style="left:331px">
  <svg class="abs" width="231" height="117" viewBox="0 0 231 117" aria-hidden="true"><path d="M0 0H231V110Q115.5 58 0 110Z" fill="url(#silver)"/><path d="M0 110Q115.5 58 231 110V117Q115.5 66 0 117Z" fill="#ddd"/></svg>
  <h2>Search</h2>
  <div class="abs search-field"></div>
  <svg class="abs" style="left:154px;top:48px" width="20" height="20" viewBox="0 0 20 20" aria-hidden="true"><circle cx="8" cy="8" r="5.5" fill="#cfe3f5" stroke="#5a6c80" stroke-width="2"/><path d="M12 12L18 18" stroke="#b07a2a" stroke-width="3" stroke-linecap="round"/></svg>
  <div class="abs go-btn">GO</div>
</section>

<section class="abs panel" style="left:574px">
  <svg class="abs" width="231" height="117" viewBox="0 0 231 117" aria-hidden="true"><path d="M0 0H231V110Q115.5 58 0 110Z" fill="url(#silver)"/><path d="M0 110Q115.5 58 231 110V117Q115.5 66 0 117Z" fill="#ddd"/></svg>
  <h2>Customer Services</h2>
  <ul class="abs svc" style="left:59px;top:35px"><li>ABOUT US</li><li>PRODUCT SHEETS</li><li>LOGIN / REGISTER</li></ul>
</section>

<aside class="abs box" style="top:470px;height:252px">
  <div class="box-head">CATEGORIES</div>
  <ul class="cats">
    <li>CORDED CURTAIN POLES</li><li>UNCORDED CURTAIN POLES</li><li>POLES WITH GLIDERS</li>
    <li>POLES WITH RINGS</li><li>CORDED CURTAIN TRACKS</li><li>UNCORDED CURTAIN TRACKS</li>
    <li>ELECTRIC CURTAIN TRACKS</li><li>ACCESSORIES</li><li>FINIALS &amp; MIDIALS</li><li>HOLDBACKS</li>
  </ul>
</aside>

<aside class="abs box" style="top:736px;height:126px">
  <div class="box-head" style="padding-top:11px">NEWSLETTER</div>
  <div class="abs field" style="left:32px;top:50px;width:154px;height:24px"></div>
  <div class="abs btn" style="left:66px;top:86px;width:86px;height:22px;line-height:22px">SUBSCRIBE</div>
</aside>

<h1 class="abs welcome" style="font-weight:400"><small>WELCOME TO</small> DOVEY RAILS</h1>
<div class="abs photo" style="left:362px;top:515px;width:139px;height:104px;background:linear-gradient(90deg,#6b3d2a,#e9d2b4 35%,#c9a77e 60%,#5a3425)" role="img" aria-label="Photo of draped curtains with a pelmet at a window"></div>
<p class="abs copy" style="left:513px;top:514px;width:296px">Lorem ipsum dolor sit amet, consectetuer adipiscing elit. Nam nibh. Nunc varius facilisis eros. Sed erat.In in velit quis arcuornare laoreet. Curabitur adipiscing luctus massa.Integer ut purus ac augue .</p>
<p class="abs copy" style="left:513px;top:584px;width:296px">Lorem ipsum dolor sit amet, consectetuer adipiscing elit. Nam nibh. Nunc varius facilisis eros. Sed erat.In in velit quis arcuornare laoreet.</p>
<p class="abs copy" style="left:364px;top:629px;width:446px">Curabitur adipiscing luctus massa.Integer ut&nbsp; purus ac augue commodo commodo. Curabitur adipiscing luctus massa.Integer ut&nbsp; purus ac augue commodo commodo.</p>

<h2 class="abs featured" style="font-weight:400">FEATURED PRODUCTS</h2>

<div class="abs photo" style="left:369px;top:729px;width:129px;height:96px;background:linear-gradient(120deg,#cfd6e0,#5d7290 45%,#34475f)" role="img" aria-label="Product photo of blue curtains on a silver track"></div>
<p class="abs product-text" style="left:374px;top:835px">Lorem ipsum dolor sit amet,<br>consectetuer adipiscin...</p>
<p class="abs price" style="left:378px;top:862px">price<b>$499.99</b></p>

<div class="abs photo" style="left:522px;top:729px;width:130px;height:96px;background:radial-gradient(circle at 55% 55%,#6a6a6a,#fafafa 60%)" role="img" aria-label="Product photo of a black cage finial on a curtain pole"></div>
<p class="abs product-text" style="left:533px;top:838px">Lorem ipsum dolor sit amet,<br>consectetuer adipiscin...</p>
<p class="abs price" style="left:537px;top:865px">price<b>$499.99</b></p>

<div class="abs photo" style="left:673px;top:729px;width:130px;height:96px;background:linear-gradient(90deg,#f4f6f5,#b9c3c0 50%,#8a5a4a 75%,#e8eceb)" role="img" aria-label="Product photo of a blind with its cord"></div>
<p class="abs product-text" style="left:685px;top:835px">Lorem ipsum dolor sit amet,<br>consectetuer adipiscin...</p>
<p class="abs price" style="left:688px;top:862px">price<b>$499.99</b></p>

<footer class="abs footer">
  <h3 style="left:47px;top:21px">QUICK CONTACT</h3>
  <div class="ff" style="left:49px;top:53px;width:109px;height:14px"></div>
  <div class="ff" style="left:49px;top:76px;width:109px;height:14px"></div>
  <div class="ff" style="left:49px;top:99px;width:109px;height:48px"></div>
  <div class="dark-btn" style="left:77px;top:157px;width:45px;height:18px;line-height:16px">SUBMIT</div>

  <h3 style="left:275px;top:21px">OUR SERVICES</h3>
  <ul>
    <li>Curabitur adipiscing luctus massa commodo.</li><li>Curabitur adipiscing luctus massa commodo.</li>
    <li>Curabitur adipiscing luctus massa commodo.</li><li>Curabitur adipiscing luctus massa commodo.</li>
    <li>Curabitur adipiscing luctus massa commodo.</li>
  </ul>

  <h3 style="left:564px;top:21px">SPECIAL OFFER<br>SIGN UP</h3>
  <div class="ff" style="left:564px;top:68px;width:119px;height:18px;border:1px solid #888"></div>
  <div class="dark-btn" style="left:693px;top:68px;width:30px;height:18px;line-height:16px">GO</div>

  <h3 style="left:567px;top:113px">FREE SAMPLE</h3>
  <div class="abs" style="left:570px;top:137px;width:38px;height:47px;background:linear-gradient(90deg,#5a1e1e,#c89b5a 45%,#ddd 70%,#333)" role="img" aria-label="Fabric swatch samples"></div>
  <p class="abs" style="left:621px;top:141px;font-size:9px;line-height:18px;color:#eee">Click here to your<br>Free Sawtches</p>
</footer>

<section class="abs base">
  <div class="abs badge" style="left:103px;top:25px;width:58px"></div>
  <div class="abs badge" style="left:164px;top:25px"></div>
  <div class="abs badge" style="left:196px;top:25px;background:#f0e2d8"></div>
  <div class="abs social" style="left:117px;top:65px;background:#3b5998"></div>
  <div class="abs social" style="left:141px;top:65px;background:#3aa9d9"></div>
  <div class="abs social" style="left:166px;top:65px;background:#2a78b8"></div>
  <div class="abs social" style="left:190px;top:65px;background:#e98a1c"></div>
  <p class="abs" style="left:406px;top:31px;font-size:9px;color:#ddd">Privacy Policy&nbsp;&nbsp; |&nbsp;&nbsp;&nbsp; Contacts&nbsp;&nbsp;&nbsp; |&nbsp;&nbsp;&nbsp; Terms and conditions of use</p>
  <p class="abs" style="left:447px;top:54px;font-size:9px;color:#ddd">© 2011 DoveyRails,&nbsp; All Rights Reserved</p>
</section>

</body>
</html>
```